Proposal Microsoft Word Template

We are looking for a professional, 5 page document to import our proposals onto. We are looking for a cover page with plenty of color and design built around and utilizing our logo. The remaining four pages should utilize our logo and have some design elements to make it stand apart from other formal proposals. We aren't sure what this looks like yet, so we are open to plenty of ideas. I will upload our logo for your use. We are a fire protection company that sells primarily to other commercial clientele.

First page will be the cover page. This should have our logo prominently placed. A place for the clients name and info.
Second page will be the Executive Summary. Smaller logo, possibly a border on this page, and a clean colorful ribbon on the footer with our information on the bottom. I do like red, blue and black for colors.

Third page will be material lists and pricing information

4th page will consist of detailed scope of work, and exclusions
Fifth page will consist of terms and conditions

Target Market(s)

Commercial Industrial Government Sectors

Requirements
Must have
• Color, clean lines and formatting.

```html
<!DOCTYPE html>
<html lang="en">
<head>
<meta charset="utf-8">
<title>Beacon Fire and Safety – Proposal Template</title>
<link rel="stylesheet" href="https://fonts.googleapis.com/css2?family=Roboto+Condensed:wght@700&family=Lato:wght@400;700&display=swap">
<style>
  :root{
    --red:#a8202a;
    --red-mid:#c9545c;
    --red-light:#e3a6aa;
    --ink:#1a1a1a;
    --text:#3b3b3b;
    --charcoal:#404040;
    --backdrop:#c2c2c2;
    --paper:#ffffff;
    --rule:#d9d9d9;
  }
  *{margin:0;padding:0;box-sizing:border-box}
  html,body{width:1200px;height:1101px;overflow:hidden;background:var(--backdrop)}
  body{position:relative;font-family:"Lato",sans-serif;color:var(--text)}
  .page{position:absolute;width:378px;height:534px;background:var(--paper);overflow:hidden}
  .page--cover{left:0;top:0}
  .page--summary{left:411px;top:0}
  .page--lists{left:822px;top:0}
  .page--data{left:0;top:566px}
  .page--contact{left:411px;top:566px;background:var(--charcoal)}

  .page-title{position:absolute;left:25px;top:22px;font-family:"Roboto Condensed",sans-serif;font-weight:700;font-size:15px;color:var(--red);letter-spacing:.2px}
  .section-title{font-family:"Roboto Condensed",sans-serif;font-weight:700;font-size:7px;color:var(--red);margin-bottom:6px}
  .copy{font-size:5.9px;line-height:1.55;text-align:justify;color:var(--text)}
  .copy p+p{margin-top:6px}

  .brand{position:absolute;font-family:"Lato",sans-serif;font-weight:700;color:var(--red);line-height:1}
  .brand__name{display:block;font-size:16px;letter-spacing:1.5px}
  .brand__tag{display:block;font-size:6px;letter-spacing:2.2px;margin-top:2px}
  .brand--small .brand__name{font-size:12px;letter-spacing:1px}
  .brand--small .brand__tag{font-size:4.6px;letter-spacing:1.5px}

  .footer-band{position:absolute;left:0;bottom:0;width:100%;height:16px;background:var(--red);color:#fff;font-size:5px;text-align:right;padding:6px 28px 0 0}

  /* cover */
  .cover__title{position:absolute;left:25px;top:22px;font-family:"Roboto Condensed",sans-serif;font-weight:700;font-size:19px;color:var(--ink)}
  .cover__subtitle{position:absolute;left:25px;top:47px;font-size:11px;color:#555}
  .cover__art{position:absolute;left:0;top:83px;width:378px;height:383px;background:radial-gradient(circle at 50% 45%,#5a5a3a 0%,#4a4a34 40%,#3a3a30 70%,#2f2f2f 100%)}
  .cover .brand{right:25px;top:480px;text-align:left}

  /* summary */
  .summary__intro{position:absolute;left:25px;top:78px;width:329px}
  .summary__text{position:absolute;left:25px;top:212px;width:329px}
  .summary__cols{display:flex;gap:18px}
  .summary__cols .copy{flex:1}
  .quote-band{position:absolute;left:0;top:372px;width:378px;height:100px;background:var(--charcoal);color:#fff;padding:8px 25px 0}
  .quote-band__mark{font-family:Georgia,serif;font-size:16px;text-align:center;line-height:1}
  .quote-band__text{font-size:7.3px;line-height:1.5;text-align:justify;margin-top:4px}
  .quote-band__mark--end{margin-top:3px}
  .page--summary .brand,.page--lists .brand{left:25px;top:490px}

  /* lists */
  .feature-list{position:absolute;left:24px;top:76px;width:330px;list-style:none}
  .feature-list li{display:flex;align-items:flex-start;height:37px}
  .feature-icon{flex:0 0 34px;height:34px;border-radius:50%;margin-right:12px;margin-top:-1px;display:flex;align-items:center;justify-content:center}
  .feature-icon--peach{background:#f7d6b4}
  .feature-icon--sky{background:#b9e4f2}
  .feature-icon--navy{background:#2c3e55}
  .feature-icon--pale{background:#e9eef2}
  .feature-list .copy{font-size:5.8px;text-align:left;padding-top:2px}
  .bullets{position:absolute;left:25px;top:280px;width:329px;list-style:none}
  .bullets li{position:relative;padding-left:9px;font-size:5.8px;line-height:1.55;margin-bottom:7px}
  .bullets li::before{content:"";position:absolute;left:0;top:3px;width:2.5px;height:2.5px;background:var(--red)}
  .bullets .sub{padding-left:19px;margin-bottom:7px}
  .bullets .sub::before{left:10px;top:4px;width:4px;height:.6px;background:#888}

  /* data */
  .data-block{position:absolute;left:24px;width:330px}
  .data-table{width:100%;border-collapse:collapse;font-size:5.2px}
  .data-table th{font-weight:700;text-align:right;padding:3px 3px}
  .data-table td{text-align:right;padding:3.2px 3px;border-bottom:.6px solid var(--rule)}
  .data-table th:first-child,.data-table td:first-child{text-align:left}
  .data-table--plain thead th{border-bottom:1px solid var(--red);color:#333}
  .data-table--boxed{border:1px solid var(--red)}
  .data-table--boxed thead th{background:var(--red);color:#fff}
  .data-table--boxed td:first-child{border-right:.6px solid var(--rule)}
  .chart{display:block}
  .page--data .brand{left:25px;top:498px}

  /* contact */
  .contact__title{position:absolute;left:0;top:22px;width:100%;text-align:center;font-family:"Roboto Condensed",sans-serif;font-weight:700;font-size:15px;color:#fff}
  .contact__intro{position:absolute;left:25px;top:80px;width:329px}
  .contact__intro .copy{color:#d6d6d6}
  .contact-item{position:absolute;left:0;width:100%;text-align:center;color:#fff;font-size:7.3px}
  .contact-item__icon{display:block;width:18px;height:18px;margin:0 auto 8px;border-radius:50%;background:var(--red);box-shadow:0 0 0 2px rgba(168,32,42,.35)}
  .page--contact .brand{left:0;width:100%;text-align:center;top:480px;color:#cfcfcf}
  .page--contact .brand__name{font-size:18px;letter-spacing:2px}
  .page--contact .brand__tag{font-size:6.5px;letter-spacing:2.6px}
</style>
</head>
<body>

<!-- Cover -->
<section class="page page--cover cover">
  <h1 class="cover__title">PROJECT TITLE GOES HERE</h1>
  <p class="cover__subtitle">Project subtitle goes here</p>
  <div class="cover__art" role="img" aria-label="Illustration: fire safety icons arranged in a ring around a shield with a flame, over a photo of a firefighter"></div>
  <div class="brand"><span class="brand__name">BEACON</span><span class="brand__tag">FIRE AND SAFETY</span></div>
</section>

<!-- Executive summary -->
<section class="page page--summary">
  <h2 class="page-title">PAGE TITLE GOES HERE</h2>
  <div class="summary__intro copy">
    <p>Lorem ipsum dolor sit amet, consectetur adipiscing elit, sed do eiusmod tempor incididunt ut labore et dolore magna aliqua. Ut enim ad minim veniam, quis nostrud exercitation ullamco laboris nisi ut aliquip ex ea commodo consequat. Duis aute irure dolor in reprehenderit in voluptate velit esse cillum dolore eu fugiat nulla pariatur. Excepteur sint occaecat cupidatat non proident, sunt in culpa qui officia deserunt mollit anim id est laborum.</p>
    <p>Sed ut perspiciatis unde omnis iste natus error sit voluptatem accusantium doloremque laudantium, totam rem aperiam, eaque ipsa quae ab illo inventore veritatis et quasi architecto beatae vitae dicta sunt explicabo. Nemo enim ipsam voluptatem quia voluptas sit aspernatur aut odit aut fugit, sed quia consequuntur magni dolores eos qui ratione voluptatem sequi nesciunt. Neque porro quisquam est, qui dolorem ipsum quia dolor sit amet, consectetur, adipisci velit, sed quia non numquam eius modi tempora incidunt ut labore et dolore magnam aliquam quaerat voluptatem. Ut enim ad minima veniam, quis nostrum exercitationem ullam corporis suscipit laboriosam, nisi ut aliquid ex ea commodi consequatur? Quis autem vel eum iure reprehenderit qui in ea voluptate velit esse quam nihil molestiae consequatur, vel illum qui dolorem eum fugiat quo voluptas nulla pariatur?</p>
  </div>
  <div class="summary__text">
    <h3 class="section-title">TEXT TITLE</h3>
    <div class="summary__cols">
      <div class="copy">
        <p>Lorem ipsum dolor sit amet, consectetur adipiscing elit, sed do eiusmod tempor incididunt ut labore et dolore magna aliqua. Ut enim ad minim veniam, quis nostrud exercitation ullamco laboris nisi ut aliquip ex ea commodo consequat. Duis aute irure dolor in reprehenderit in voluptate velit esse cillum dolore eu fugiat nulla pariatur. Excepteur sint occaecat cupidatat non proident, sunt in culpa qui officia deserunt mollit anim id est laborum.</p>
        <p>Sed ut perspiciatis unde omnis iste natus error sit voluptatem accusantium doloremque laudantium, totam rem aperiam, eaque ipsa quae ab illo inventore veritatis et quasi architecto beatae vitae dicta sunt</p>
      </div>
      <div class="copy">
        <p>explicabo. Nemo enim ipsam voluptatem quia voluptas sit aspernatur aut odit aut fugit, sed quia consequuntur magni dolores eos qui ratione voluptatem sequi nesciunt. Neque porro quisquam est, qui dolorem ipsum quia dolor sit amet, consectetur, adipisci velit, sed quia non numquam eius modi tempora incidunt ut labore et dolore magnam aliquam quaerat voluptatem. Ut enim ad minima veniam, quis nostrum exercitationem ullam corporis suscipit laboriosam, nisi ut aliquid ex ea commodi consequatur? Quis autem vel eum iure reprehenderit qui in ea voluptate velit esse quam nihil molestiae consequatur, vel illum qui dolorem eum fugiat quo voluptas nulla pariatur?</p>
      </div>
    </div>
  </div>
  <blockquote class="quote-band">
    <div class="quote-band__mark">&ldquo;</div>
    <p class="quote-band__text">Lorem ipsum dolor sit amet, consectetur adipiscing elit, sed do eiusmod tempor incididunt ut labore et dolore magna aliqua. Ut enim ad minim veniam, quis nostrud exercitation ullamco laboris nisi ut aliquip ex ea commodo consequat. Duis aute irure dolor in reprehenderit in voluptate velit esse cillum dolore eu fugiat nulla pariatur. Excepteur sint occaecat cupidatat non proident, sunt in culpa qui officia deserunt mollit anim id est laborum.</p>
    <div class="quote-band__mark quote-band__mark--end">&rdquo;</div>
  </blockquote>
  <div class="brand brand--small"><span class="brand__name">BEACON</span><span class="brand__tag">FIRE AND SAFETY</span></div>
  <div class="footer-band">02</div>
</section>

<!-- Material lists -->
<section class="page page--lists">
  <h2 class="page-title">PAGE TITLE GOES HERE</h2>
  <ul class="feature-list">
    <li><span class="feature-icon feature-icon--peach" role="img" aria-label="Flame icon"><svg width="14" height="16" viewBox="0 0 14 16"><path d="M7 0C8 4 13 6 13 10a6 6 0 0 1-12 0C1 7 4 6 4 3c2 1 3 3 3 5 1-2 1-5 0-8z" fill="#e0492e"/></svg></span><p class="copy">Lorem ipsum dolor sit amet, consectetur adipiscing elit, sed do eiusmod tempor incididunt ut labore et dolore magna aliqua. Ut enim ad minim veniam, quis nostrud exercitation ullamco laboris nisi ut aliquip ex ea commodo consequat.</p></li>
    <li><span class="feature-icon feature-icon--sky" role="img" aria-label="Extinguisher icon"><svg width="10" height="18" viewBox="0 0 10 18"><rect x="2" y="4" width="6" height="14" rx="2" fill="#d63a2f"/><rect x="3" y="1" width="4" height="3" fill="#333"/></svg></span><p class="copy">Lorem ipsum dolor sit amet, consectetur adipiscing elit, sed do eiusmod tempor incididunt ut labore et dolore magna aliqua. Ut enim ad minim veniam, quis nostrud exercitation ullamco laboris nisi ut aliquip ex ea commodo consequat.</p></li>
    <li><span class="feature-icon feature-icon--navy" role="img" aria-label="Building icon"><svg width="10" height="16" viewBox="0 0 10 16"><rect x="1" y="3" width="8" height="13" fill="#4fb3e6"/><rect x="3" y="6" width="1.5" height="1.5" fill="#fff"/><rect x="5.5" y="6" width="1.5" height="1.5" fill="#fff"/><rect x="3" y="9" width="1.5" height="1.5" fill="#fff"/><rect x="5.5" y="9" width="1.5" height="1.5" fill="#fff"/></svg></span><p class="copy">Lorem ipsum dolor sit amet, consectetur adipiscing elit, sed do eiusmod tempor incididunt ut labore et dolore magna aliqua. Ut enim ad minim veniam, quis nostrud exercitation ullamco laboris nisi ut aliquip ex ea commodo consequat.</p></li>
    <li><span class="feature-icon feature-icon--pale" role="img" aria-label="Exit sign icon"><svg width="24" height="12" viewBox="0 0 24 12"><rect x="0.5" y="0.5" width="23" height="11" rx="1" fill="#d63a2f"/><text x="12" y="9" font-family="Lato,sans-serif" font-size="8" fill="#fff" text-anchor="middle">EXIT</text></svg></span><p class="copy">Lorem ipsum dolor sit amet, consectetur adipiscing elit, sed do eiusmod tempor incididunt ut labore et dolore magna aliqua. Ut enim ad minim veniam, quis nostrud exercitation ullamco laboris nisi ut aliquip ex ea commodo consequat.</p></li>
    <li><span class="feature-icon feature-icon--navy" role="img" aria-label="House icon"><svg width="16" height="14" viewBox="0 0 16 14"><path d="M8 0L16 7H14V14H2V7H0Z" fill="#fff"/><path d="M8 6c1 2 3 3 3 5a3 3 0 0 1-6 0c0-2 2-3 3-5z" fill="#e0492e"/></svg></span><p class="copy">Lorem ipsum dolor sit amet, consectetur adipiscing elit, sed do eiusmod tempor incididunt ut labore et dolore magna aliqua. Ut enim ad minim veniam, quis nostrud exercitation ullamco laboris nisi ut aliquip ex ea commodo consequat.</p></li>
  </ul>
  <ul class="bullets">
    <li>Lorem ipsum dolor sit amet, consectetur adipiscing elit, sed do eiusmod tempor incididunt ut labore et dolore magna aliqua.</li>
    <li>Lorem ipsum dolor sit amet, consectetur adipiscing elit, sed do eiusmod tempor incididunt ut labore et dolore magna aliqua.</li>
    <li>Lorem ipsum dolor sit amet, consectetur adipiscing elit, sed do eiusmod tempor incididunt ut labore et dolore magna aliqua.</li>
    <li>Lorem ipsum dolor sit amet, consectetur adipiscing elit, sed do eiusmod tempor incididunt ut labore et dolore magna aliqua.</li>
    <li>Lorem ipsum dolor sit amet, consectetur adipiscing elit, sed do eiusmod tempor incididunt ut labore et dolore magna aliqua.</li>
    <li class="sub">Lorem ipsum dolor sit amet, consectetur adipiscing elit, sed do eiusmod tempor incididunt ut labore et dolore magna aliqua.</li>
    <li class="sub">Lorem ipsum dolor sit amet, consectetur adipiscing elit, sed do eiusmod tempor incididunt ut labore et dolore magna aliqua.</li>
    <li class="sub">Lorem ipsum dolor sit amet, consectetur adipiscing elit, sed do eiusmod tempor incididunt ut labore et dolore magna aliqua.</li>
    <li class="sub">Lorem ipsum dolor sit amet, consectetur adipiscing elit, sed do eiusmod tempor incididunt ut labore et dolore magna aliqua.</li>
  </ul>
  <div class="brand brand--small"><span class="brand__name">BEACON</span><span class="brand__tag">FIRE AND SAFETY</span></div>
  <div class="footer-band">03</div>
</section>

<!-- Tables and charts -->
<section class="page page--data">
  <h2 class="page-title">PAGE TITLE GOES HERE</h2>

  <div class="data-block" style="top:84px">
    <h3 class="section-title">TABLE TITLE</h3>
    <table class="data-table data-table--plain">
      <thead><tr><th>Title 1</th><th>Title 2</th><th>Title 3</th><th>Title 4</th><th>Title 5</th></tr></thead>
      <tbody>
        <tr><td>Lorem ipsum</td><td>456</td><td>57</td><td>46</td><td>213</td></tr>
        <tr><td>Lorem ipsum</td><td>356</td><td>4,548</td><td>454</td><td>34</td></tr>
        <tr><td>Lorem ipsum</td><td>54</td><td>5,645</td><td>80</td><td>57</td></tr>
        <tr><td>Lorem ipsum</td><td>23</td><td>65</td><td>-</td><td>233</td></tr>
      </tbody>
    </table>
  </div>

  <div class="data-block" style="top:189px">
    <h3 class="section-title">TABLE TITLE</h3>
    <table class="data-table data-table--boxed">
      <thead><tr><th>Title 1</th><th>Title 2</th><th>Title 3</th><th>Title 4</th><th>Title 5</th></tr></thead>
      <tbody>
        <tr><td>Lorem ipsum</td><td>456</td><td>57</td><td>46</td><td>213</td></tr>
        <tr><td>Lorem ipsum</td><td>356</td><td>4,548</td><td>454</td><td>34</td></tr>
        <tr><td>Lorem ipsum</td><td>54</td><td>5,645</td><td>80</td><td>57</td></tr>
        <tr><td>Lorem ipsum</td><td>23</td><td>65</td><td>-</td><td>233</td></tr>
      </tbody>
    </table>
  </div>

  <div class="data-block" style="top:294px">
    <h3 class="section-title">CHART TITLE</h3>
    <svg class="chart" width="330" height="80" viewBox="0 0 330 80" font-family="Lato,sans-serif" font-size="5.2" fill="#555">
      <text x="2" y="8">10</text><text x="5" y="27">5</text><text x="5" y="46">0</text>
      <line x1="12" y1="44.5" x2="330" y2="44.5" stroke="#bbb" stroke-width=".6"/>
      <g>
        <rect x="28" y="28" width="13" height="16" fill="var(--red)"/><rect x="46" y="36" width="13" height="8" fill="var(--red-mid)"/><rect x="64" y="38" width="13" height="6" fill="var(--red-light)"/>
        <rect x="107" y="35" width="13" height="9" fill="var(--red)"/><rect x="125" y="28" width="13" height="16" fill="var(--red-mid)"/><rect x="143" y="38" width="13" height="6" fill="var(--red-light)"/>
        <rect x="186" y="32" width="13" height="12" fill="var(--red)"/><rect x="204" y="38" width="13" height="6" fill="var(--red-mid)"/><rect x="222" y="34" width="13" height="10" fill="var(--red-light)"/>
        <rect x="265" y="28" width="13" height="16" fill="var(--red)"/><rect x="283" y="34" width="13" height="10" fill="var(--red-mid)"/><rect x="301" y="25" width="13" height="19" fill="var(--red-light)"/>
      </g>
      <text x="39" y="54">Category 1</text><text x="118" y="54">Category 2</text><text x="197" y="54">Category 3</text><text x="276" y="54">Category 4</text>
      <rect x="66" y="60" width="3" height="3" fill="var(--red)"/><text x="70" y="63">Series 1</text>
      <rect x="154" y="60" width="3" height="3" fill="var(--red-mid)"/><text x="158" y="63">Series 2</text>
      <rect x="243" y="60" width="3" height="3" fill="var(--red-light)"/><text x="247" y="63">Series 3</text>
    </svg>
  </div>

  <div class="data-block" style="top:399px">
    <h3 class="section-title">TABLE TITLE</h3>
    <svg class="chart" width="330" height="80" viewBox="0 0 330 80" font-family="Lato,sans-serif" font-size="5.2" fill="#555">
      <text x="2" y="8">10</text><text x="5" y="25">5</text><text x="5" y="42">0</text>
      <line x1="12" y1="40.5" x2="310" y2="40.5" stroke="#bbb" stroke-width=".6"/>
      <path d="M18 27 L116 24 L214 29 L312 32 L312 40 L18 40Z" fill="var(--red-light)"/>
      <path d="M18 32 L116 28 L214 31 L312 30 L312 40 L18 40Z" fill="var(--red-mid)"/>
      <path d="M18 35 L116 33 L214 32 L312 22 L312 40 L18 40Z" fill="var(--red)"/>
      <text x="5" y="50">Category 1</text><text x="103" y="50">Category 2</text><text x="201" y="50">Category 3</text><text x="298" y="50">Category 4</text>
      <rect x="66" y="56" width="3" height="3" fill="var(--red-light)"/><text x="70" y="59">Series 1</text>
      <rect x="154" y="56" width="3" height="3" fill="var(--red-mid)"/><text x="158" y="59">Series 2</text>
      <rect x="243" y="56" width="3" height="3" fill="var(--red)"/><text x="247" y="59">Series 3</text>
    </svg>
  </div>

  <div class="brand brand--small"><span class="brand__name">BEACON</span><span class="brand__tag">FIRE AND SAFETY</span></div>
  <div class="footer-band">04</div>
</section>

<!-- Contact -->
<section class="page page--contact">
  <h2 class="contact__title">CONTACT US</h2>
  <div class="contact__intro copy">
    <p>Lorem ipsum dolor sit amet, consectetur adipiscing elit, sed do eiusmod tempor incididunt ut labore et dolore magna aliqua. Ut enim ad minim veniam, quis nostrud exercitation ullamco laboris nisi ut aliquip ex ea commodo consequat. Duis aute irure dolor in reprehenderit in voluptate velit esse cillum dolore eu fugiat nulla pariatur. Excepteur sint occaecat cupidatat non proident, sunt in culpa qui officia deserunt mollit anim id est laborum.</p>
    <p>Sed ut perspiciatis unde omnis iste natus error sit voluptatem accusantium doloremque laudantium, totam rem aperiam, eaque ipsa quae ab illo inventore veritatis et quasi architecto beatae vitae dicta sunt explicabo. Nemo enim ipsam voluptatem quia voluptas sit aspernatur aut odit aut fugit, sed quia consequuntur magni dolores eos qui ratione voluptatem sequi nesciunt. Neque porro quisquam est, qui dolorem ipsum quia dolor sit amet, consectetur, adipisci velit, sed quia non numquam eius modi tempora incidunt ut labore et dolore magnam aliquam quaerat voluptatem. Ut enim ad minima veniam, quis nostrum exercitationem ullam corporis suscipit laboriosam, nisi ut aliquid ex ea commodi consequatur?</p>
  </div>

  <div class="contact-item" style="top:198px">
    <svg class="contact-item__icon" viewBox="0 0 18 18"><path d="M6.5 5c.5 0 1 1.5 1 2s-.8.7-.6 1.2c.4 1 1.3 1.9 2.3 2.3.5.2.7-.6 1.2-.6s2 .5 2 1-1 1.6-1.6 1.6C8 12.5 5.5 10 5 6.6 5 6 6 5 6.5 5z" fill="none" stroke="#fff" stroke-width=".8"/></svg>
    123.456.789
  </div>
  <div class="contact-item" style="top:260px">
    <svg class="contact-item__icon" viewBox="0 0 18 18"><rect x="5" y="6" width="8" height="6" fill="none" stroke="#fff" stroke-width=".8"/><path d="M5 6l4 3.5L13 6" fill="none" stroke="#fff" stroke-width=".8"/></svg>
    hello@beaconfiresafety.com
  </div>
  <div class="contact-item" style="top:331px">
    <svg class="contact-item__icon" viewBox="0 0 18 18"><circle cx="9" cy="9" r="4" fill="none" stroke="#fff" stroke-width=".8"/><path d="M5 9h8M9 5c-2 2.5-2 5.5 0 8M9 5c2 2.5 2 5.5 0 8" fill="none" stroke="#fff" stroke-width=".6"/></svg>
    www.beaconfiresafety.com
  </div>
  <div class="contact-item" style="top:400px">
    <svg class="contact-item__icon" viewBox="0 0 18 18"><path d="M9 14s-3.5-3.6-3.5-6a3.5 3.5 0 0 1 7 0c0 2.4-3.5 6-3.5 6z" fill="none" stroke="#fff" stroke-width=".8"/><circle cx="9" cy="8" r="1.2" fill="#fff"/></svg>
    123, Example street, Example
  </div>

  <div class="brand"><span class="brand__name">BEACON</span><span class="brand__tag">FIRE AND SAFETY</span></div>
</section>

</body>
</html>
```